Personal Tax Specialists Banner

We need banner adverts for a personal tax firm. We specialise in Luxembourg, US and UK personal taxation. The banner should be modern, cool, simple and illustrated.

Banner should highlight "Personal Taxation Specialists" and the countries that we specialise in, "Luxembourg", "US" and "UK".

Target Market(s)

Individuals looking for assistance with tax return preparation.

Industry/Entity Type

Finance And Accounting

Colors

Designer to choose colors to be used in the design.

Requirements
Must have
• Output in GIF.
• The main banner size is 980 x 120 and some smaller square banners (300 x 300)
• Button to link back to website www.corvinfiling.com
Nice to have
• We would like an illustrated design if possible.

```html
<!DOCTYPE html>
<html lang="en">
<head>
<meta charset="utf-8">
<title>Corvin Filing &amp; Advisory – Square Banners</title>
<link href="https://fonts.googleapis.com/css2?family=Barlow+Semi+Condensed:wght@600;700&display=swap" rel="stylesheet">
<style>
  :root {
    --page: #ffffff;
    --maroon: #7a0035;
    --orange: #f7941d;
    --yellow: #f8b22a;
    --teal: #0f98ad;
    --white: #ffffff;
    --ink: #2b2b3a;
    --flag-red: #d6262f;
    --flag-blue: #1f3d8c;
    --flag-sky: #2aa3dc;
  }
  * { box-sizing: border-box; margin: 0; padding: 0; }
  html, body {
    width: 1200px; height: 442px; overflow: hidden;
    background: var(--page);
    font-family: "Barlow Semi Condensed", "Arial Narrow", sans-serif;
  }
  .canvas { position: relative; width: 1200px; height: 442px; }

  .banner {
    position: absolute; top: 55px; width: 300px; height: 300px; overflow: hidden;
    box-shadow: -6px 6px 10px rgba(0,0,0,.18);
  }
  .banner--specialists { left: 52px; background: var(--maroon); }
  .banner--services { left: 405px; background: var(--yellow); }
  .banner--visit { left: 757px; background: var(--teal); }

  .brand {
    position: absolute; top: 15px; left: 0; right: 0;
    display: flex; justify-content: center; align-items: center; gap: 6px;
    font-weight: 600; line-height: 1;
  }
  .brand__dot { width: 22px; height: 22px; border-radius: 50%; border: 2px solid currentColor; }
  .brand__name { font-size: 15px; letter-spacing: .5px; }
  .brand__name small { display: block; font-size: 6.5px; letter-spacing: .6px; margin-top: 1px; }
  .banner--specialists .brand, .banner--visit .brand { color: var(--white); }
  .banner--services .brand { color: var(--maroon); }

  .headline {
    position: absolute; left: 0; right: 0; text-align: center;
    font-weight: 700; text-transform: uppercase; line-height: 1;
  }
  .headline__line { display: block; font-size: 29px; color: var(--white); }
  .tag { display: inline-block; padding: 2px 6px 1px; }

  .banner--specialists .headline { top: 55px; }
  .banner--specialists .tag { background: var(--orange); color: var(--white); margin-top: 4px; }

  .banner--services .headline { top: 55px; font-size: 31px; }
  .banner--services .headline__plain { color: var(--maroon); }
  .banner--services .tag { background: var(--maroon); color: var(--white); margin-left: 4px; }

  .banner--visit .headline { top: 55px; font-size: 31px; }
  .banner--visit .tag { background: var(--white); color: var(--teal); margin-right: 4px; }
  .banner--visit .headline__plain { color: var(--white); }

  .illustration { position: absolute; border-radius: 12px; }
  .banner--specialists .illustration {
    left: 90px; top: 128px; width: 120px; height: 152px;
    background: linear-gradient(180deg, rgba(247,148,29,.55), rgba(255,255,255,.25));
  }
  .banner--services .illustration {
    left: 80px; top: 100px; width: 140px; height: 100px;
    background: linear-gradient(180deg, rgba(255,255,255,.55), rgba(43,43,58,.25));
  }
  .banner--visit .illustration {
    left: 40px; top: 100px; width: 220px; height: 130px;
    background: linear-gradient(180deg, rgba(255,255,255,.45), rgba(43,43,58,.3));
  }

  .countries {
    position: absolute; top: 210px; left: 0; right: 0;
    display: flex; justify-content: center; gap: 26px; list-style: none;
  }
  .country { width: 52px; text-align: center; color: var(--maroon); font-weight: 700; font-size: 9.5px; text-transform: uppercase; }
  .country__flag { display: block; width: 52px; height: 52px; margin: 0 auto 6px; }

  .cta {
    position: absolute; left: 0; right: 0; bottom: 10px; height: 45px;
    background: var(--white); border-radius: 22px 0 0 0;
    display: flex; align-items: center; justify-content: center;
    color: var(--teal); font-weight: 700; font-size: 27px; text-decoration: none;
  }
</style>
</head>
<body>
<main class="canvas">

  <section class="banner banner--specialists">
    <div class="brand"><span class="brand__dot"></span><span class="brand__name">CORVIN<small>FILING &amp; ADVISORY</small></span></div>
    <h1 class="headline">
      <span class="headline__line">Personal Taxation</span>
      <span class="tag headline__line">Specialists</span>
    </h1>
    <div class="illustration" role="img" aria-label="Illustration of a tax adviser at a desk with paperwork and floating finance icons"></div>
  </section>

  <section class="banner banner--services">
    <div class="brand"><span class="brand__dot"></span><span class="brand__name">CORVIN<small>FILING &amp; ADVISORY</small></span></div>
    <h2 class="headline"><span class="headline__plain">Our</span><span class="tag">Services</span></h2>
    <div class="illustration" role="img" aria-label="Illustration of two advisers working together at a computer screen showing a chart"></div>
    <ul class="countries">
      <li class="country">
        <svg class="country__flag" viewBox="0 0 52 52" role="img" aria-label="Luxembourg flag">
          <defs><clipPath id="clip-lu"><circle cx="26" cy="26" r="24"/></clipPath></defs>
          <g clip-path="url(#clip-lu)">
            <rect x="0" y="0" width="52" height="18" fill="var(--flag-red)"/>
            <rect x="0" y="18" width="52" height="16" fill="#fff"/>
            <rect x="0" y="34" width="52" height="18" fill="var(--flag-sky)"/>
          </g>
          <circle cx="26" cy="26" r="24" fill="none" stroke="var(--maroon)" stroke-width="3"/>
        </svg>Luxembourg
      </li>
      <li class="country">
        <svg class="country__flag" viewBox="0 0 52 52" role="img" aria-label="United States flag">
          <defs><clipPath id="clip-us"><circle cx="26" cy="26" r="24"/></clipPath></defs>
          <g clip-path="url(#clip-us)">
            <rect x="0" y="0" width="52" height="52" fill="#fff"/>
            <g fill="var(--flag-red)">
              <rect x="0" y="0" width="52" height="4"/>
              <rect x="0" y="8" width="52" height="4"/>
              <rect x="0" y="16" width="52" height="4"/>
              <rect x="0" y="24" width="52" height="4"/>
              <rect x="0" y="32" width="52" height="4"/>
              <rect x="0" y="40" width="52" height="4"/>
              <rect x="0" y="48" width="52" height="4"/>
            </g>
            <rect x="0" y="0" width="26" height="28" fill="var(--flag-blue)"/>
            <g fill="#fff">
              <circle cx="8" cy="8" r="1.1"/><circle cx="13" cy="8" r="1.1"/><circle cx="18" cy="8" r="1.1"/><circle cx="23" cy="8" r="1.1"/>
              <circle cx="10.5" cy="12.5" r="1.1"/><circle cx="15.5" cy="12.5" r="1.1"/><circle cx="20.5" cy="12.5" r="1.1"/>
              <circle cx="8" cy="17" r="1.1"/><circle cx="13" cy="17" r="1.1"/><circle cx="18" cy="17" r="1.1"/><circle cx="23" cy="17" r="1.1"/>
              <circle cx="10.5" cy="21.5" r="1.1"/><circle cx="15.5" cy="21.5" r="1.1"/><circle cx="20.5" cy="21.5" r="1.1"/>
            </g>
          </g>
          <circle cx="26" cy="26" r="24" fill="none" stroke="var(--maroon)" stroke-width="3"/>
        </svg>USA
      </li>
      <li class="country">
        <svg class="country__flag" viewBox="0 0 52 52" role="img" aria-label="United Kingdom flag">
          <defs><clipPath id="clip-uk"><circle cx="26" cy="26" r="24"/></clipPath></defs>
          <g clip-path="url(#clip-uk)">
            <rect x="0" y="0" width="52" height="52" fill="var(--flag-blue)"/>
            <path d="M0 0 L52 52 M52 0 L0 52" stroke="#fff" stroke-width="10"/>
            <path d="M0 0 L52 52 M52 0 L0 52" stroke="var(--flag-red)" stroke-width="3.5"/>
            <path d="M26 0 V52 M0 26 H52" stroke="#fff" stroke-width="14"/>
            <path d="M26 0 V52 M0 26 H52" stroke="var(--flag-red)" stroke-width="8"/>
          </g>
          <circle cx="26" cy="26" r="24" fill="none" stroke="var(--maroon)" stroke-width="3"/>
        </svg>UK
      </li>
    </ul>
  </section>

  <section class="banner banner--visit">
    <div class="brand"><span class="brand__dot"></span><span class="brand__name">CORVIN<small>FILING &amp; ADVISORY</small></span></div>
    <h2 class="headline"><span class="tag">Visit</span><span class="headline__plain">Us</span></h2>
    <div class="illustration" role="img" aria-label="Illustration of a team meeting around a table beneath a light bulb with a percent sign and business icons"></div>
    <a class="cta" href="https://www.corvinfiling.com">www.corvinfiling.com</a>
  </section>

</main>
</body>
</html>
```